Business card for apparel company. Specializing in fishing and boating performance wear. Main company name is Marlow Pelican Company, LLC brand name for apparel is TIDEWAKE. See website www.TidewakeBayline.com I will attach some logos to consider.

```html
<!DOCTYPE html>
<html lang="en">
<head>
<meta charset="utf-8">
<title>TIDEWAKE Business Card</title>
<link rel="stylesheet" href="https://fonts.googleapis.com/css2?family=Montserrat:wght@400;500;700;800&family=Oswald:wght@600&display=swap">
<style>
  :root {
    --stage: #d3d3d3;
    --paper: #ffffff;
    --sea: #a7cbc8;
    --sea-edge: #8fbdb9;
    --navy: #3a4a5c;
    --ink: #1f1f1f;
    --rule: #2b2b2b;
  }
  * { margin: 0; padding: 0; box-sizing: border-box; }
  html, body { width: 1200px; height: 892px; overflow: hidden; }
  body {
    background: var(--stage);
    font-family: "Montserrat", sans-serif;
    color: var(--navy);
    position: relative;
  }
  .card {
    position: absolute;
    width: 520px;
    height: 297px;
    border-radius: 24px;
    box-shadow: 0 14px 30px rgba(0,0,0,0.22);
    overflow: hidden;
  }
  /* Front */
  .card-front {
    left: 60px; top: 170px;
    background: var(--paper);
    border: 2px solid var(--sea-edge);
  }
  .brand-lockup {
    position: absolute;
    display: flex; align-items: center; gap: 12px;
  }
  .brand-lockup .dot {
    width: 34px; height: 34px; border-radius: 50%;
    background: var(--sea);
  }
  .brand-lockup .name {
    font-weight: 800; color: var(--navy); letter-spacing: 1px;
  }
  .card-front .brand-lockup { right: 34px; top: 52px; }
  .card-front .brand-lockup .name { font-size: 34px; }
  .front-rule {
    position: absolute; left: 30px; right: 30px; top: 138px;
    height: 1.5px; background: var(--rule);
  }
  .person { position: absolute; left: 34px; top: 160px; }
  .person-name { font-size: 22px; font-weight: 700; letter-spacing: 0.5px; }
  .person-title { font-size: 13px; color: var(--ink); margin-top: 2px; }
  .person-rule { width: 190px; height: 1.5px; background: var(--rule); margin: 10px 0 8px; }
  .contacts { list-style: none; }
  .contacts li {
    display: flex; align-items: center; gap: 8px;
    font-size: 12.5px; color: var(--ink); line-height: 20px;
  }
  .contacts svg { width: 12px; height: 12px; fill: var(--navy); flex: none; }
  .address {
    position: absolute; right: 34px; top: 160px;
    font-size: 13px; color: var(--ink); line-height: 20px; text-align: left;
  }
  /* Back */
  .card-back {
    left: 620px; top: 420px;
    background: var(--sea);
  }
  .card-back .brand-lockup {
    left: 0; right: 0; top: 88px; justify-content: center;
  }
  .card-back .brand-lockup .dot { width: 48px; height: 48px; background: var(--navy); }
  .card-back .brand-lockup .name { font-size: 50px; }
  .tagline {
    position: absolute; left: 0; right: 0; bottom: 40px;
    text-align: center;
    font-family: "Oswald", sans-serif; font-weight: 600;
    font-size: 17px; color: var(--ink); letter-spacing: 0.3px;
  }
</style>
</head>
<body>
  <section class="card card-front" aria-label="Card front">
    <div class="brand-lockup">
      <span class="dot"></span>
      <span class="name">TIDEWAKE</span>
    </div>
    <div class="front-rule"></div>
    <div class="person">
      <p class="person-name">AVERY QUINN</p>
      <p class="person-title">Managing Director</p>
      <div class="person-rule"></div>
      <ul class="contacts">
        <li><svg viewBox="0 0 24 24"><path d="M6.6 10.8a15 15 0 0 0 6.6 6.6l2.2-2.2a1 1 0 0 1 1-.25 11.4 11.4 0 0 0 3.6.6 1 1 0 0 1 1 1V20a1 1 0 0 1-1 1A17 17 0 0 1 3 4a1 1 0 0 1 1-1h3.5a1 1 0 0 1 1 1c0 1.25.2 2.45.6 3.6a1 1 0 0 1-.25 1z"/></svg>044-321 654 987</li>
        <li><svg viewBox="0 0 24 24"><path d="M2 5h20v14H2z M2 5l10 8 10-8" /></svg>info@marlowpelican.com</li>
        <li><svg viewBox="0 0 24 24"><circle cx="12" cy="12" r="10"/></svg>www.TidewakeBayline.com</li>
      </ul>
    </div>
    <p class="address">421, Address line here<br>Country Name, 45452</p>
  </section>

  <section class="card card-back" aria-label="Card back">
    <div class="brand-lockup">
      <span class="dot"></span>
      <span class="name">TIDEWAKE</span>
    </div>
    <p class="tagline">SPECIALIZING IN FISHING AND BOATING PERFORMANCE WEAR</p>
  </section>
</body>
</html>
```